Redesign our business card for more impact

We want to completely replace the back design of our card, and refresh or even change the front entirely. We are happy with our black Q7 logo and do not want to change it.
Our company address changed too. It is now 58 Corvallen, Irvine, CA 92741
Updates

It was reported by Sketch Harbor email today that the uploaded files didnt upload. I am trying again.

Target Market(s)

Architects and Building Owners (People making multi-million dollar decisions)

Industry/Entity Type

Consulting Engineering

Contact Information for Business Card

Contact info on the front. "wallpaper" design on back with tag line on the back "Engineering Your Future"

Font styles to use
Sans Serif

Requirements
Must have
• A vivid, modern, impactful ...but tasteful back of card design. It should communicate our premier status, but grab attention as innovative. DESIGN SHOULD BE ELEGANT AND NOT TOO BUSY.
Nice to have
• Repeating pattern, multi-color, something creative...
Should not have
• Anything that looks too playful or that we are not serious professionals. It should also not be too boring or conservative.

```html
<!DOCTYPE html>
<html lang="en">
<head>
<meta charset="utf-8">
<title>Q7 Business Card</title>
<link rel="stylesheet" href="https://fonts.googleapis.com/css2?family=Poppins:wght@400;600;700&display=swap">
<style>
  :root {
    --page-bg: #161617;
    --card-bg: #2a2a2d;
    --card-bg-deep: #18181a;
    --ink-light: #f4f4f4;
    --ink-soft: #dcdcdc;
    --back-mark: #3c3c40;
    --band: #3a3a3e;
    --band-edge: #0f0f10;
    --tagline: #121213;
  }
  * { box-sizing: border-box; margin: 0; padding: 0; }
  html, body { width: 1200px; height: 801px; overflow: hidden; }
  body {
    background: var(--page-bg);
    font-family: "Poppins", sans-serif;
    display: flex;
    align-items: center;
    justify-content: center;
    gap: 40px;
  }
  .card {
    position: relative;
    width: 540px;
    height: 309px;
    border-radius: 16px;
    background: linear-gradient(155deg, var(--card-bg) 0%, var(--card-bg-deep) 100%);
    box-shadow: 0 18px 40px rgba(0, 0, 0, 0.55);
    overflow: hidden;
  }

  /* Front */
  .brand-mark {
    position: absolute;
    left: 44px;
    top: 82px;
    font-weight: 700;
    font-size: 128px;
    line-height: 1;
    letter-spacing: -4px;
    color: var(--ink-light);
  }
  .divider {
    position: absolute;
    left: 262px;
    top: 56px;
    width: 1px;
    height: 190px;
    background: var(--ink-soft);
  }
  .contact {
    position: absolute;
    left: 284px;
    top: 52px;
    color: var(--ink-light);
  }
  .contact__name {
    font-weight: 600;
    font-size: 21px;
    letter-spacing: 0.5px;
    line-height: 1.15;
  }
  .contact__role { font-size: 14px; line-height: 1.3; }
  .contact__creds { font-size: 10.5px; line-height: 1.4; color: var(--ink-soft); }
  .contact__address {
    margin-top: 16px;
    font-size: 12px;
    line-height: 1.4;
    color: var(--ink-soft);
  }
  .contact__lines { margin-top: 14px; list-style: none; }
  .contact__lines li {
    display: flex;
    align-items: center;
    gap: 7px;
    font-size: 12.5px;
    line-height: 1.55;
  }
  .contact__lines svg { width: 12px; height: 12px; flex: none; }

  /* Back */
  .back__mark {
    position: absolute;
    left: 0;
    right: 0;
    top: 34px;
    text-align: center;
    font-weight: 700;
    font-size: 148px;
    line-height: 1;
    letter-spacing: -6px;
    color: var(--back-mark);
  }
  .back__band {
    position: absolute;
    left: 0;
    right: 0;
    top: 212px;
    height: 50px;
    background: var(--band);
    border-bottom: 4px solid var(--band-edge);
    display: flex;
    align-items: center;
    justify-content: center;
  }
  .back__tagline {
    font-weight: 700;
    font-size: 26px;
    letter-spacing: 1.5px;
    color: var(--tagline);
  }
</style>
</head>
<body>
  <section class="card card--front" aria-label="Card front">
    <div class="brand-mark">Q7</div>
    <div class="divider"></div>
    <div class="contact">
      <p class="contact__name">DYLAN VARGA</p>
      <p class="contact__role">CEO</p>
      <p class="contact__creds">PE, HFDP, LEED AP</p>
      <p class="contact__address">58 Corvallen, Irvine<br>CA 92741</p>
      <ul class="contact__lines">
        <li>
          <svg viewBox="0 0 12 12" aria-hidden="true"><rect x="0.5" y="0.5" width="11" height="11" rx="2" fill="none" stroke="#f4f4f4"/><path d="M3.5 3 L5 3 L5.5 4.6 L4.7 5.2 Q5.5 6.8 6.8 7.3 L7.4 6.5 L9 7 L9 8.5 Q5 8.8 3.5 3 Z" fill="#f4f4f4"/></svg>
          +255 4316 0872
        </li>
        <li>
          <svg viewBox="0 0 12 12" aria-hidden="true"><rect x="0.5" y="0.5" width="11" height="11" rx="2" fill="none" stroke="#f4f4f4"/><circle cx="6" cy="6" r="3.2" fill="none" stroke="#f4f4f4" stroke-width="0.9"/><path d="M2.8 6 H9.2 M6 2.8 Q4.3 6 6 9.2 M6 2.8 Q7.7 6 6 9.2" fill="none" stroke="#f4f4f4" stroke-width="0.7"/></svg>
          q7eng.com
        </li>
        <li>
          <svg viewBox="0 0 12 12" aria-hidden="true"><rect x="0.5" y="0.5" width="11" height="11" rx="2" fill="none" stroke="#f4f4f4"/><rect x="2.5" y="3.5" width="7" height="5" fill="none" stroke="#f4f4f4" stroke-width="0.9"/><path d="M2.5 3.5 L6 6.3 L9.5 3.5" fill="none" stroke="#f4f4f4" stroke-width="0.9"/></svg>
          dylan.varga@q7eng.com
        </li>
      </ul>
    </div>
  </section>

  <section class="card card--back" aria-label="Card back">
    <div class="back__mark">Q7</div>
    <div class="back__band">
      <p class="back__tagline">ENGINEERING YOUR FUTURE</p>
    </div>
  </section>
</body>
</html>
```